KTR Global corporate slide deck

We are looking for a custom powerpoint template to use both internally and externally with clients and during trainings/presentations. Our customers/clients often include a lot of government agencies, and we specialize in forensics, biometrics, and identity intelligence.
Requirements:
• Title slide
• Section slide
• Title and content slide
• Every slide branded
• Every slide (other than title) includes slide number (x of y), title, and date
• Modern-looking but conservative
• Visually appealing
• Source Sans Pro font
• Call out boxes

The circle in our logo does not signify or mean anything in any way, but we also don't mind it being used as a design element. We also like pulling the blue to red gradient.
Ideally we do not want to use any images of people, but iconography is likely okay.

```html
<!DOCTYPE html>
<html lang="en">
<head>
<meta charset="utf-8">
<title>KTR Global – Title Slide</title>
<link href="https://fonts.googleapis.com/css2?family=Oswald:wght@200;300&family=Source+Sans+3:wght@400;600;700&display=swap" rel="stylesheet">
<style>
  :root {
    --blue: #4338e6;
    --violet: #6c3fd6;
    --purple: #8a3fbf;
    --magenta: #9a3380;
    --crimson: #8e2a3e;
    --ring-dark: #262b48;
    --ring-teal: #2f6f86;
    --ring-warm: #c9865e;
    --inner-glow: rgba(150, 90, 220, 0.35);
    --white: #ffffff;
    --logo-tint: #f1e4f4;
  }
  * { margin: 0; padding: 0; box-sizing: border-box; }
  html, body {
    width: 1200px; height: 675px; overflow: hidden;
    background: #1a1530;
  }
  .slide {
    position: relative;
    width: 1200px; height: 675px;
    overflow: hidden;
    font-family: "Source Sans 3", "Source Sans Pro", sans-serif;
    color: var(--white);
  }
  .backdrop {
    position: absolute; inset: 0;
    background:
      radial-gradient(ellipse 40% 55% at 58% 62%, rgba(120, 70, 200, 0.55), transparent 70%),
      linear-gradient(90deg, var(--blue) 0%, var(--violet) 35%, var(--purple) 58%, var(--magenta) 80%, var(--crimson) 100%);
  }
  .hero-ring {
    position: absolute;
    left: 298px; top: 38px;
    width: 604px; height: 604px;
  }
  .title-block {
    position: absolute;
    left: 360px; top: 300px;
    width: 480px;
    text-align: center;
  }
  .presentation-title {
    font-family: "Oswald", sans-serif;
    font-weight: 200;
    font-size: 52px;
    line-height: 1;
    letter-spacing: 0.5px;
    text-transform: uppercase;
  }
  .presentation-subtitle {
    width: 262px;
    margin: 18px auto 0;
    font-weight: 700;
    font-size: 13.5px;
    line-height: 1.22;
  }
  .brand {
    position: absolute;
    left: 30px; top: 532px;
    display: flex; align-items: center; gap: 14px;
  }
  .brand-mark {
    width: 74px; height: 74px;
    border-radius: 50%;
    border: 6px solid var(--logo-tint);
  }
  .brand-name {
    font-weight: 700;
    font-size: 30px;
    color: var(--logo-tint);
    letter-spacing: 0.3px;
  }
</style>
</head>
<body>
  <main class="slide">
    <div class="backdrop" role="img" aria-label="Background photo of a fingertip touching a glowing digital fingerprint scan, washed in a blue to red gradient"></div>

    <svg class="hero-ring" viewBox="0 0 604 604" role="img" aria-label="Ring-shaped window showing the fingerprint scan photo">
      <defs>
        <linearGradient id="ringFill" x1="0" y1="0" x2="0.6" y2="1">
          <stop offset="0" stop-color="var(--ring-warm)"/>
          <stop offset="0.35" stop-color="#6a4a8e"/>
          <stop offset="0.7" stop-color="var(--ring-teal)"/>
          <stop offset="1" stop-color="var(--ring-dark)"/>
        </linearGradient>
        <radialGradient id="innerGlow" cx="0.5" cy="0.5" r="0.5">
          <stop offset="0" stop-color="rgba(170,110,230,0.35)"/>
          <stop offset="1" stop-color="rgba(120,70,200,0.15)"/>
        </radialGradient>
      </defs>
      <circle cx="302" cy="302" r="240" fill="url(#innerGlow)"/>
      <path fill="url(#ringFill)" fill-rule="evenodd" opacity="0.92"
        d="M302 0a302 302 0 1 0 0.01 0Z M302 62a240 240 0 1 1 -0.01 0Z"/>
    </svg>

    <section class="title-block">
      <h1 class="presentation-title">Presentation Title</h1>
      <p class="presentation-subtitle">Lorem ipsum dolor sit amet, consetetur sadipscing elitr, sed diam nonumy eirmod tempor invidunt ut labore et dolore magna.</p>
    </section>

    <div class="brand">
      <span class="brand-mark"></span>
      <span class="brand-name">KTR Global</span>
    </div>
  </main>
</body>
</html>
```